Strong, modern, clean Business Card design

Looking for a stunning, but CLEAN business card design. While we are a faith-based organization, we do NOT want this to look religious.

Industry/Entity Type

Non-Profit

Contact Information for Business Card

Dale Munroe | Lead Pastor
dale@BrightHarvestHope.org
970-555-0148
PO Box 7316
Loveland, CO 80571

Font styles to use
Serif
Sans Serif

Requirements
Should not have
• Religious imagery or symbolism

```html
<!DOCTYPE html>
<html lang="en">
<head>
<meta charset="utf-8">
<title>Evergreen Gathering – Business Card</title>
<link rel="stylesheet" href="https://fonts.googleapis.com/css2?family=Cinzel:wght@500&family=EB+Garamond:wght@400;700&display=swap">
<style>
  :root {
    --backdrop: #2b2b2b;
    --card-white: #ffffff;
    --teal: #4b8399;
    --teal-deep: #3f7489;
    --ink-light: #ffffff;
    --ink-soft: #e3eef2;
  }
  * { margin: 0; padding: 0; box-sizing: border-box; }
  html, body {
    width: 1200px;
    height: 898px;
    overflow: hidden;
    background: var(--backdrop);
  }
  .canvas {
    position: relative;
    width: 1200px;
    height: 898px;
    display: flex;
    align-items: center;
    justify-content: center;
  }
  .business-card {
    position: relative;
    width: 1000px;
    height: 571px;
    border-radius: 26px;
    overflow: hidden;
    background: var(--card-white);
  }
  .brand {
    position: absolute;
    top: 78px;
    left: 0;
    width: 100%;
    text-align: center;
    color: var(--teal);
    font-family: "Cinzel", serif;
    font-weight: 500;
  }
  .brand-primary {
    display: block;
    font-size: 76px;
    letter-spacing: 4px;
    line-height: 1;
  }
  .brand-secondary {
    display: block;
    margin-top: 14px;
    font-size: 30px;
    letter-spacing: 38px;
    padding-left: 38px;
    line-height: 1;
  }
  .divider-stripes {
    position: absolute;
    left: 0;
    top: 258px;
    width: 100%;
    height: 28px;
  }
  .stripe {
    position: absolute;
    left: 0;
    width: 100%;
    height: 6px;
    background: var(--teal);
  }
  .stripe-one { top: 0; }
  .stripe-two { top: 11px; }
  .info-panel {
    position: absolute;
    left: 0;
    top: 280px;
    width: 100%;
    height: 291px;
    background: var(--teal);
    color: var(--ink-light);
    font-family: "EB Garamond", serif;
    text-align: center;
  }
  .identity {
    margin-top: 44px;
    display: flex;
    justify-content: center;
    align-items: center;
    gap: 16px;
  }
  .person-name {
    font-weight: 700;
    font-size: 25px;
    letter-spacing: 1px;
    text-transform: uppercase;
  }
  .identity-bar {
    width: 2px;
    height: 36px;
    background: var(--ink-light);
  }
  .person-role {
    font-size: 21px;
    color: var(--ink-soft);
  }
  .rule {
    width: 600px;
    height: 2px;
    margin: 22px auto 0;
    background: var(--ink-light);
  }
  .contact-row {
    margin-top: 26px;
    display: flex;
    justify-content: center;
    gap: 44px;
    font-size: 21px;
    color: var(--ink-soft);
  }
  .contact-item {
    display: flex;
    align-items: center;
    gap: 10px;
  }
  .contact-icon {
    width: 20px;
    height: 20px;
    fill: var(--ink-light);
  }
  .address {
    margin-top: 16px;
    font-weight: 700;
    font-size: 25px;
    letter-spacing: 0.5px;
  }
</style>
</head>
<body>
<main class="canvas">
  <article class="business-card">
    <header class="brand">
      <span class="brand-primary">EVERGREEN</span>
      <span class="brand-secondary">GATHERING</span>
    </header>

    <div class="divider-stripes">
      <span class="stripe stripe-one"></span>
      <span class="stripe stripe-two"></span>
    </div>

    <section class="info-panel">
      <div class="identity">
        <span class="person-name">Dale Munroe</span>
        <span class="identity-bar"></span>
        <span class="person-role">Lead Pastor</span>
      </div>

      <div class="rule"></div>

      <div class="contact-row">
        <span class="contact-item">
          <svg class="contact-icon" viewBox="0 0 24 24" aria-hidden="true">
            <path d="M3 9c0-3 4-5 9-5s9 2 9 5v2h-5V9c-1-.6-2.4-1-4-1s-3 .4-4 1v2H3z"/>
            <path d="M7 12h10l3 8H4z"/>
          </svg>
          970-555-0148
        </span>
        <span class="contact-item">
          <svg class="contact-icon" viewBox="0 0 24 24" aria-hidden="true">
            <path d="M2 5h20v14H2z" />
            <path d="M2 5l10 8 10-8" fill="none" stroke="#4b8399" stroke-width="1.8"/>
          </svg>
          dale@BrightHarvestHope.org
        </span>
      </div>

      <div class="rule"></div>

      <p class="address">PO Box 7316 , Loveland, CO 80571</p>
    </section>
  </article>
</main>
</body>
</html>
```